Mobile App UI Redesign for Service Booking app

Bookora is a business management system made especially for service based businesses (our subscribers). It enables systemising your service businesses. This can be used by diverse industries like automotive service, beauty (hair salons, nail spas), Spas, Chiropractor, acupuntcure, osteo, yoga studio, business coach, etc.

One component of this management system is a consumer app that the users (customers of our subscribers) can use to book in services with businesses (subscribers). Any business that provides services, either 1-to-1(personal training/ hair cut, etc) or 1-to-many (classes/ sessions)can get their users to download the app and book straight away in real time.

The current app is built as a version that is available to all subscribers. Hence the search screen at the beginning of the app. Our subscribers have the option to brand this app, with their own logo and colours.

The UI of the app needs to be designed using flat and clean UI design trends that are currently prevailing for B2C apps. Even the sliding menu panel can be removed and alternative placement of this functionality can be suggested. The color palette used for the design should be limited (3-5 colours) so that minimum effort is required to convert this into our customers branded app.

The Current UI screens are open to suggestions for change. For ease of booking in minimum steps, consolidation of functionality on different screens can be suggested, accompanies by a rational reason with the objective of having a simple and straight forward user experience.

User should be able to move from one function to another (booking > view appointments > profile) in no more than 1 or max 2 gestures.

Target Market(s)

Service Based Businesses that require customers to book in services or sessions with them. These can include health services (chiro, physio, osteo, accupuncture, etc) Beauty (hair salon, nail spa, health spa, etc) automotive service (car service, motorcycle service, bike service, etc)

Industry/Entity Type

Business

Requirements
Must have
• Design files to be delivered in JPG and Vectored PSD format

```html
<!DOCTYPE html>
<html lang="en">
<head>
<meta charset="utf-8">
<title>Bookora – App Screens</title>
<link href="https://fonts.googleapis.com/css2?family=Arimo:wght@400;700&display=swap" rel="stylesheet">
<style>
:root{
  --stage:#6a6a6a;
  --brand:#f7941d;
  --brand-dark:#e5800a;
  --white:#ffffff;
  --surface:#ececec;
  --line:#d6d6d6;
  --muted:#8a8a8a;
  --alert:#e53935;
  --ink:#333333;
}
*{box-sizing:border-box;margin:0;padding:0}
html,body{width:747px;height:1200px;overflow:hidden}
body{background:var(--stage);font-family:"Arimo",Helvetica,Arial,sans-serif;position:relative}
.screen{position:absolute;width:320px;background:var(--white);overflow:hidden;display:flex;flex-direction:column}
.screen--search{left:40px;top:25px;height:565px}
.screen--detail{left:387px;top:25px;height:565px;background:var(--surface)}
.screen--results{left:40px;top:605px;height:560px;background:var(--surface)}
.screen--menu{left:387px;top:605px;height:560px;background:var(--surface)}

.topbar{background:var(--brand);color:var(--white);flex:none}
.status{height:20px;display:flex;align-items:center;justify-content:space-between;padding:0 6px;font-size:9px}
.status .carrier{display:flex;align-items:center;gap:3px}
.status .right{display:flex;align-items:center;gap:4px}
.nav{height:38px;display:flex;align-items:center;position:relative;padding:0 10px}
.nav .title{position:absolute;left:0;right:0;text-align:center;font-size:16px;pointer-events:none}
.nav .back{font-size:12px;display:flex;align-items:center;gap:2px}
.nav .cancel{font-size:12px;margin-left:auto}
.nav .search-pill{margin-left:10px;flex:1;height:20px;background:var(--white);border-radius:4px;display:flex;align-items:center;gap:4px;padding:0 6px;font-size:9px;color:var(--muted)}

/* search form */
.form{padding:50px 44px 0;display:flex;flex-direction:column;gap:24px}
.field{height:38px;border:2px solid var(--brand);border-radius:4px;display:flex;align-items:center;padding:0 8px;color:var(--brand);font-size:12px;font-weight:700}
.btn{background:var(--brand);color:var(--white);font-weight:700;border-radius:3px;display:flex;align-items:center;justify-content:center}
.btn--search{width:82px;height:34px;margin:6px auto 0;font-size:15px}

/* detail */
.hero{margin:6px 6px 0;height:162px;background:var(--white);border-radius:12px;display:flex;align-items:center;justify-content:center;color:var(--brand);font-size:44px;box-shadow:0 1px 2px rgba(0,0,0,.15)}
.info{padding:16px 16px 0;color:var(--brand);font-size:11px;line-height:1.35}
.info-row{display:flex;align-items:flex-start;gap:8px;margin-bottom:12px}
.info-row .ico{width:16px;flex:none;display:flex;justify-content:center}
.dot{width:7px;height:7px;border-radius:50%;background:var(--alert);margin-top:3px}
.blurb{padding-left:24px;margin-bottom:10px}
.fav{display:flex;align-items:center;gap:8px;color:var(--muted);padding-left:24px}
.fav .box{width:10px;height:10px;border:1px solid var(--muted);background:var(--white)}
.btn--select{margin:16px 24px 0;height:30px;font-size:12px;font-weight:400}

/* results */
.list{list-style:none}
.row{height:37px;background:var(--white);border-bottom:1px solid var(--line)}
.row--item{height:58px;display:flex;align-items:center;gap:8px;padding:0 6px}
.thumb{width:38px;height:38px;border:1px solid var(--line);display:flex;align-items:center;justify-content:center;font-size:10px;color:var(--brand)}
.item-text{color:var(--brand);font-size:8px;line-height:1.25}
.item-text .name{font-size:10px}
.item-text .phone{display:flex;align-items:center;gap:3px;color:var(--muted);font-size:7px;margin-top:2px}

/* menu */
.menu-body{flex:1;display:flex}
.drawer{width:258px;background:var(--brand);color:var(--white);padding-top:14px}
.menu-item{display:flex;align-items:center;gap:8px;padding:0 12px;height:34px;font-size:15px}
.menu-item svg{flex:none}
.hamburger{display:flex;flex-direction:column;gap:3px}
.hamburger span{width:16px;height:2px;background:var(--white)}
</style>
</head>
<body>

<!-- Screen: search -->
<section class="screen screen--search">
  <header class="topbar">
    <div class="status">
      <span class="carrier">●●●●○ CELL</span><span>4:21 PM</span>
      <span class="right">100% <svg width="18" height="8" viewBox="0 0 18 8"><rect x=".5" y=".5" width="15" height="7" rx="1" fill="none" stroke="#fff"/><rect x="2" y="2" width="12" height="4" fill="#fff"/><rect x="16" y="2.5" width="1.5" height="3" fill="#fff"/></svg></span>
    </div>
    <div class="nav"><span class="title">App Name</span></div>
  </header>
  <form class="form">
    <div class="field">Search Services By Name</div>
    <div class="field">Select City</div>
    <div class="field">Select Business Type</div>
    <div class="field">Select Postal Code</div>
    <div class="btn btn--search">Search</div>
  </form>
</section>

<!-- Screen: business detail -->
<section class="screen screen--detail">
  <header class="topbar">
    <div class="status">
      <span class="carrier">●●●●○ CELL</span><span>4:21 PM</span>
      <span class="right">100% <svg width="18" height="8" viewBox="0 0 18 8"><rect x=".5" y=".5" width="15" height="7" rx="1" fill="none" stroke="#fff"/><rect x="2" y="2" width="12" height="4" fill="#fff"/><rect x="16" y="2.5" width="1.5" height="3" fill="#fff"/></svg></span>
    </div>
    <div class="nav"><span class="back">‹Back</span><span class="title">Lorem ipsum</span></div>
  </header>
  <div class="hero" role="img" aria-label="Business cover image">Image</div>
  <div class="info">
    <div class="info-row">
      <span class="ico"><svg width="14" height="14" viewBox="0 0 24 24"><circle cx="12" cy="12" r="11" fill="none" stroke="#555" stroke-width="1.5"/><path d="M8 6l2 0 1 3-1.5 1a7 7 0 0 0 3.5 3.5l1-1.5 3 1 0 2a2 2 0 0 1-2 2A10 10 0 0 1 6 8a2 2 0 0 1 2-2z" fill="#555"/></svg></span>
      <span>130055501299</span>
    </div>
    <div class="info-row">
      <span class="ico"><span class="dot"></span></span>
      <span>Lorem ipsum dolor sit amet, consectetuer adipiscing elit. Aliquam tincidunt mauris eu risus.</span>
    </div>
    <p class="blurb">Morbi in sem quis dui placerat ornare. Pellentesque odio nisi, euismod in, pharetra a, ultricies in, diam. Sed arcu. Cras consequat.</p>
    <div class="fav"><span class="box"></span>Remove From Favourites</div>
  </div>
  <div class="btn btn--select">Select Business</div>
</section>

<!-- Screen: search results -->
<section class="screen screen--results">
  <header class="topbar">
    <div class="status">
      <span class="carrier">●●●●○ CELL</span><span>4:21 PM</span>
      <span class="right">100% <svg width="18" height="8" viewBox="0 0 18 8"><rect x=".5" y=".5" width="15" height="7" rx="1" fill="none" stroke="#fff"/><rect x="2" y="2" width="12" height="4" fill="#fff"/><rect x="16" y="2.5" width="1.5" height="3" fill="#fff"/></svg></span>
    </div>
    <div class="nav">
      <span class="back">‹Back</span>
      <span class="search-pill"><svg width="9" height="9" viewBox="0 0 10 10"><circle cx="4" cy="4" r="3" fill="none" stroke="#888" stroke-width="1.3"/><path d="M6.3 6.3 9 9" stroke="#888" stroke-width="1.3"/></svg>Search business by name</span>
      <span class="cancel">&nbsp;Cancel</span>
    </div>
  </header>
  <ul class="list">
    <li class="row row--item">
      <div class="thumb" role="img" aria-label="Business thumbnail">Image</div>
      <div class="item-text">
        <div class="name">Lorem ipsum</div>
        <div>Lorem ipsum dolor sit amet consectetuer</div>
        <div>adipiscing elit</div>
        <div class="phone"><svg width="7" height="7" viewBox="0 0 24 24"><path d="M6 3l4 0 2 5-2.5 1.5a11 11 0 0 0 5 5L16 12l5 2 0 4a3 3 0 0 1-3 3A17 17 0 0 1 3 6a3 3 0 0 1 3-3z" fill="#888"/></svg>130055501299</div>
      </div>
    </li>
    <li class="row"></li><li class="row"></li><li class="row"></li><li class="row"></li>
    <li class="row"></li><li class="row"></li><li class="row"></li><li class="row"></li>
    <li class="row"></li><li class="row"></li><li class="row"></li><li class="row"></li>
  </ul>
</section>

<!-- Screen: side menu -->
<section class="screen screen--menu">
  <header class="topbar">
    <div class="status">
      <span class="carrier">●●●●○ CELL</span><span>4:21 PM</span>
      <span class="right">100% <svg width="18" height="8" viewBox="0 0 18 8"><rect x=".5" y=".5" width="15" height="7" rx="1" fill="none" stroke="#fff"/><rect x="2" y="2" width="12" height="4" fill="#fff"/><rect x="16" y="2.5" width="1.5" height="3" fill="#fff"/></svg></span>
    </div>
    <div class="nav"><span class="hamburger"><span></span><span></span><span></span></span><span class="title">Lorem ipsum</span></div>
  </header>
  <div class="menu-body">
    <nav class="drawer">
      <div class="menu-item"><svg width="18" height="18" viewBox="0 0 24 24"><circle cx="12" cy="12" r="11" fill="#fff"/><circle cx="12" cy="9" r="4" fill="#f7941d"/><path d="M5 19a7 6 0 0 1 14 0" fill="#f7941d"/></svg>User Profile</div>
      <div class="menu-item"><svg width="18" height="18" viewBox="0 0 24 24"><path d="M12 2l3 7 7 .6-5.3 4.6 1.6 7.3L12 17.8 5.7 21.5l1.6-7.3L2 9.6 9 9z" fill="#fff"/></svg>Favourite Companies</div>
      <div class="menu-item"><svg width="18" height="18" viewBox="0 0 24 24"><circle cx="10" cy="10" r="7" fill="none" stroke="#fff" stroke-width="2.5"/><path d="M15 15l6 6" stroke="#fff" stroke-width="3"/></svg>Seach Company</div>
      <div class="menu-item"><svg width="18" height="18" viewBox="0 0 24 24"><rect x="3" y="5" width="18" height="16" rx="2" fill="#fff"/><rect x="3" y="5" width="18" height="4" fill="#fde3c3"/><rect x="7" y="2" width="2" height="5" fill="#fff"/><rect x="15" y="2" width="2" height="5" fill="#fff"/></svg>Appointment</div>
    </nav>
  </div>
</section>

</body>
</html>
```